Online Rug Store needs Clearance Banner

Website is: Lanternfield Carpets and Home
You can access it at: www.lanternfieldcarpetsandhome.com and login (top right) with password: trazok

*** update: When creating banners for my site, you have permission to use images from www.velbora.com, but ONLY for this project. The images/artwork are copyright allowable for use on www.lanternfieldcarpetsandhome.com projects.***

We need a home page banner sized 1000 wide x 500 tall pixels to promote a "Clearance Sale" on rugs. The banner can state:

1. Clearance Sale
2. Now in progress
3. Save an extra 20% with coupon code 'Mint20'
4. Ends March 31st
5. Plus Free Shipping and 30 day returns.

We prefer a banner that appears hand-drawn and artistic, not commercially produced. It is OK to use a room scene image, rug images, or just a colored/textured background with text and no images. Your choice.

Flat graphics with no shadows and 3-D effect preferred.
Attached is are 3 logo options, as well as an example banner with handcrafted, artistic styling that we prefer.

Target Market(s)

This should be an eye-catching banner to showcase a very urgent promotion. Consider using colors of red, white, gold, and black to make a strong statement on the home page.

Industry/Entity Type

Home And Garden

Requirements
Must have
• Winner must provide Photoshop editable file format (.psd format) including layers that can be edited.
Nice to have
• Hand-drawn, stenciled, scribbled, artistic graphics and fonts is nice because we sell rugs that are made by hand.
Should not have
• little to no shadowing. Avoid computerized graphics.

```html
<!DOCTYPE html>
<html lang="en">
<head>
<meta charset="utf-8">
<title>Clearance Sale – Lanternfield Carpets and Home</title>
<link rel="stylesheet" href="https://fonts.googleapis.com/css2?family=Cinzel:wght@400&family=Dosis:wght@400;500&family=Montserrat:wght@500;800&family=Permanent+Marker&display=swap">
<style>
  :root {
    --sand-light: #f6d8a8;
    --sand-mid: #e8c794;
    --sand-deep: #c9a67a;
    --maroon: #7a1414;
    --gold-top: #f2ec9a;
    --gold-bottom: #b29a3a;
    --olive-gold: #9c8a3c;
    --ink: #111111;
    --paper: #ffffff;
  }
  html, body {
    margin: 0;
    width: 1200px;
    height: 600px;
    overflow: hidden;
    background: var(--sand-light);
  }
  .banner {
    position: relative;
    width: 1000px;
    height: 500px;
    transform: scale(1.2);
    transform-origin: 0 0;
    overflow: hidden;
    font-family: "Dosis", sans-serif;
  }
  .rug-backdrop {
    position: absolute;
    inset: 0;
    background:
      linear-gradient(90deg, var(--sand-light) 0%, var(--sand-light) 28%, rgba(246,216,168,0.55) 45%, rgba(246,216,168,0) 70%),
      linear-gradient(180deg, var(--sand-mid) 0%, var(--sand-deep) 100%);
  }
  .headline-clearance {
    position: absolute;
    left: 58px;
    top: 92px;
    margin: 0;
    font-family: "Dosis", sans-serif;
    font-weight: 400;
    font-size: 76px;
    line-height: 1;
    letter-spacing: 1px;
    color: var(--maroon);
  }
  .headline-sale {
    position: absolute;
    left: 40px;
    top: 170px;
    margin: 0;
    font-family: "Permanent Marker", cursive;
    font-size: 200px;
    line-height: 1;
    transform: skewX(-14deg) rotate(-6deg);
    background: linear-gradient(180deg, var(--gold-top), var(--gold-bottom));
    -webkit-background-clip: text;
    background-clip: text;
    color: transparent;
  }
  .end-date {
    position: absolute;
    left: 130px;
    top: 428px;
    margin: 0;
    font-size: 22px;
    font-weight: 500;
    color: var(--maroon);
    letter-spacing: 0.5px;
  }
  .brand-block {
    position: absolute;
    left: 657px;
    top: 0;
    width: 318px;
    height: 93px;
    background: var(--ink);
    display: flex;
    align-items: center;
    gap: 12px;
    padding-left: 38px;
    box-sizing: border-box;
  }
  .brand-mark {
    width: 30px;
    height: 30px;
    background: var(--paper);
    flex: none;
  }
  .brand-name {
    font-family: "Cinzel", serif;
    font-size: 19px;
    line-height: 1.1;
    color: var(--paper);
  }
  .menu-icon {
    position: absolute;
    left: 758px;
    top: 256px;
  }
  .offer-eyebrow {
    position: absolute;
    left: 663px;
    top: 310px;
    margin: 0;
    font-family: "Montserrat", sans-serif;
    font-weight: 500;
    font-size: 9px;
    letter-spacing: 0.5px;
    color: var(--ink);
  }
  .offer-save {
    position: absolute;
    left: 659px;
    top: 326px;
    margin: 0;
    font-family: "Montserrat", sans-serif;
    font-weight: 800;
    font-size: 44px;
    line-height: 1;
    color: var(--ink);
  }
  .offer-extra {
    position: absolute;
    left: 660px;
    top: 372px;
    margin: 0;
    font-family: "Montserrat", sans-serif;
    font-weight: 500;
    font-size: 25px;
    line-height: 1;
    color: var(--ink);
  }
  .offer-percent {
    position: absolute;
    left: 786px;
    top: 322px;
    margin: 0;
    font-family: "Montserrat", sans-serif;
    font-weight: 800;
    font-size: 88px;
    line-height: 1;
    letter-spacing: -2px;
    color: var(--olive-gold);
  }
  .coupon-bar {
    position: absolute;
    left: 657px;
    top: 410px;
    width: 333px;
    height: 30px;
    background: var(--ink);
    color: var(--paper);
    font-family: "Montserrat", sans-serif;
    font-weight: 800;
    font-size: 14.5px;
    letter-spacing: 1px;
    display: flex;
    align-items: center;
    padding-left: 10px;
    box-sizing: border-box;
  }
  .perks-bar {
    position: absolute;
    left: 657px;
    top: 445px;
    width: 333px;
    height: 55px;
    background: var(--ink);
    color: var(--paper);
    padding: 6px 10px 0;
    box-sizing: border-box;
  }
  .perks-lead {
    display: block;
    font-size: 11px;
    line-height: 1.2;
  }
  .perks-main {
    display: block;
    font-size: 21px;
    line-height: 1.3;
    letter-spacing: 0.5px;
  }
</style>
</head>
<body>
  <main class="banner">
    <div class="rug-backdrop" role="img" aria-label="Photograph of handmade striped rugs in tan, brown and black, fading into a sand-coloured background"></div>

    <h1 class="headline-clearance">CLEARANCE</h1>
    <p class="headline-sale">SALE</p>
    <p class="end-date">ENDS MARCH 31ST</p>

    <div class="brand-block">
      <span class="brand-mark"></span>
      <span class="brand-name">Lanternfield<br>Carpets and Home</span>
    </div>

    <svg class="menu-icon" width="28" height="28" viewBox="0 0 28 28" aria-hidden="true">
      <rect x="0" y="3" width="28" height="4" fill="#111"/>
      <rect x="0" y="12" width="28" height="4" fill="#111"/>
      <rect x="0" y="21" width="28" height="4" fill="#111"/>
    </svg>

    <p class="offer-eyebrow">NOW IN PROGRESS:</p>
    <p class="offer-save">SAVE</p>
    <p class="offer-extra">AN EXTRA</p>
    <p class="offer-percent">20%</p>

    <div class="coupon-bar">WITH COUPON CODE 'MINT20'</div>
    <div class="perks-bar">
      <span class="perks-lead">PLUS FREE</span>
      <span class="perks-main">SHIPPING &amp; 30 DAY RETURNS</span>
    </div>
  </main>
</body>
</html>
```